Business card and stationary design for a digital advertising agency

We look to get designs for
- Business card
- Envelope C5 & A4
- Letterhead A4
- Thin Folder (to place the brochures and quotes in. There must be places to put the cd envelope and a business card inside the file as well as a place for the papers)
- CD label & envelope
- Notepad
- Mousepad

We are open for all kind of creativity but please have a look at our website to have an idea. (The website is not ready at the moment but you can see the colours, get the logo, etc.)

Link: www.plexaroth.com/anasayfa

PLEASE NOTE: In the logo file, there are 2 logos but we only use the one on top. We never use the one at the bottom!
Updates

Please use the attached ForDesign.zip file to use the background pattern of our website, inside the folder img there are background patterns of our website. Please use the background or at least inspire from that files in order to design our brochures.  

All designers, please bear in mind that firstly we need the samples of each items described in the brief. Then we will comment on each of them. 

Please submit the designs for all the items at once.

Thanks!

KorvilTek

Target Market(s)

Our customers are the companies who will advertise on internet and digital media and we work mainly in Turkish market

Industry/Entity Type

Digital

Requirements
Must have
• Please use the attached ForDesign.zip file to use the background pattern of our website, inside the folder img there are background patterns of our website. Please use the background or at least inspire from that files in order to design our brochures.
Should not have
• Too much colours such as a child's colouring book.

```html
<!DOCTYPE html>
<html lang="en">
<head>
<meta charset="utf-8">
<title>KorvilTek Stationery</title>
<link rel="stylesheet" href="https://fonts.googleapis.com/css2?family=Nunito+Sans:wght@400;700;800&display=swap">
<style>
  :root {
    --paper: #ffffff;
    --ink: #1a1a1a;
    --brand-grey: #4a4a4c;
    --link: #c2187a;
    --night: #070707;
    --shadow: rgba(0, 0, 0, 0.28);
  }
  html, body {
    margin: 0;
    width: 1200px;
    height: 541px;
    overflow: hidden;
    background: var(--paper);
    font-family: "Nunito Sans", Arial, sans-serif;
    color: var(--ink);
  }
  .stage { position: relative; width: 1200px; height: 541px; }
  .sheet {
    position: absolute;
    background: var(--paper);
    box-shadow: 3px 4px 6px var(--shadow);
  }
  .letterhead { left: 55px; top: 65px; width: 328px; height: 421px; }
  .envelope-a4 { left: 143px; top: 118px; width: 423px; height: 325px; }
  .envelope-c5 { left: 309px; top: 215px; width: 328px; height: 155px; }
  .card-front { left: 520px; top: 238px; width: 151px; height: 85px; }
  .card-back {
    left: 687px; top: 238px; width: 148px; height: 85px;
    background: radial-gradient(ellipse at 40% 60%, #6a1030 0%, #2a0a2a 35%, var(--night) 75%);
  }
  .folder {
    left: 850px; top: 63px; width: 325px; height: 423px;
    background:
      radial-gradient(circle at 30% 20%, rgba(230,40,40,0.55) 0%, transparent 22%),
      radial-gradient(circle at 55% 45%, rgba(240,200,40,0.45) 0%, transparent 25%),
      radial-gradient(circle at 80% 35%, rgba(60,200,60,0.35) 0%, transparent 22%),
      radial-gradient(circle at 25% 55%, rgba(70,80,220,0.4) 0%, transparent 25%),
      radial-gradient(circle at 45% 70%, rgba(200,40,90,0.35) 0%, transparent 25%),
      var(--night);
    box-shadow: none;
  }
  .small {
    position: absolute;
    font-size: 5.5px;
    line-height: 1.35;
    font-weight: 700;
    margin: 0;
  }
  .link { color: var(--link); }
  .wordmark {
    position: absolute;
    margin: 0;
    font-weight: 800;
    color: var(--brand-grey);
    letter-spacing: -0.02em;
    line-height: 1;
  }
  .wordmark.on-dark { color: var(--paper); }
  .mark-dot {
    display: inline-block;
    width: 0.28em; height: 0.28em;
    background: currentColor;
    border-radius: 50%;
    margin-left: 0.12em;
    vertical-align: 0.9em;
  }
</style>
</head>
<body>
<main class="stage">

  <section class="sheet letterhead" aria-label="Letterhead A4">
    <p class="small" style="left:8px; top:8px;">info@plexaroth.com<br><span class="link">www.plexaroth.com</span></p>
    <p class="small" style="left:119px; top:8px;">Levent Caddesi, Akasya Mahallesi<br>No 48 Kat 3 Ortaköy, Istanbul</p>
    <p class="small" style="left:259px; top:8px;">T +90 212 555 0142<br>F +90 212 555 0143</p>
    <p class="wordmark" style="right:14px; bottom:12px; font-size:22px;">KorvilTek<span class="mark-dot"></span></p>
  </section>

  <section class="sheet envelope-a4" aria-label="Envelope A4">
    <p class="small" style="left:8px; top:11px;">Levent Caddesi,<br>Akasya Mahallesi<br>No 48 Kat 3<br>Ortaköy, Istanbul<br><span class="link">www.plexaroth.com</span></p>
    <p class="wordmark" style="right:14px; bottom:12px; font-size:22px;">KorvilTek<span class="mark-dot"></span></p>
  </section>

  <section class="sheet envelope-c5" aria-label="Envelope C5">
    <p class="small" style="left:6px; top:11px;">Levent Caddesi,<br>Akasya Mahallesi<br>No 48 Kat 3<br>Ortaköy, Istanbul<br><span class="link">www.plexaroth.com</span></p>
    <p class="wordmark" style="right:11px; bottom:9px; font-size:17px;">KorvilTek<span class="mark-dot"></span></p>
  </section>

  <section class="sheet card-front" aria-label="Business card front">
    <p class="small" style="left:3px; top:4px; font-size:4px;"><span class="link">Deniz Arslan</span><br>Director<br><br>deniz@plexaroth.com<br>M +90 532 555 0178</p>
    <p class="small" style="left:78px; top:4px; font-size:4px;">Levent Caddesi,<br>Akasya Mahallesi<br>No 48 Kat 3<br>Ortaköy, Istanbul<br>T +90 212 555 0142<br>F +90 212 555 0143<br><span class="link">www.plexaroth.com</span></p>
    <p class="wordmark" style="right:15px; bottom:6px; font-size:10px;">KorvilTek<span class="mark-dot"></span></p>
  </section>

  <div class="sheet card-back" role="img" aria-label="Card back with glowing coloured square pattern on black"></div>

  <section class="sheet folder" aria-label="Folder cover">
    <div role="img" aria-label="Glowing translucent coloured squares scattered across a black background" style="position:absolute; inset:0;"></div>
    <p class="wordmark on-dark" style="right:16px; bottom:16px; font-size:22px;">KorvilTek<span class="mark-dot"></span></p>
  </section>

</main>
</body>
</html>
```